Plumbing Business needs a more appealing business card design and logo

card must include phone number and logo, open to new logo ideas, full creative freedom

Industry/Entity Type

Plumbing

Contact Information for Business Card

Darrell Whitcombe
0417305829

Logo Text

call outs from $80

Font styles to use
• unsure

Colors
ec1f27
0255a3
f78f20

```html
<!DOCTYPE html>
<html lang="en">
<head>
<meta charset="UTF-8">
<title>Halden's Plumbing – Business Card</title>
<link href="https://fonts.googleapis.com/css2?family=Oswald:wght@500;600&family=Roboto:wght@400&display=swap" rel="stylesheet">
<style>
  :root {
    --backdrop: #18191c;
    --card: #1f2326;
    --orange: #f78f20;
    --blue: #0d5fb0;
    --blue-text: #1f5fae;
  }
  * { margin: 0; padding: 0; box-sizing: border-box; }
  html, body {
    width: 1200px; height: 800px; overflow: hidden;
    background: var(--backdrop);
  }
  .stage {
    width: 1200px; height: 800px;
    display: flex; align-items: center; justify-content: center; gap: 48px;
  }
  .card {
    width: 525px; height: 300px;
    background: var(--card);
    position: relative;
    box-shadow: 0 18px 40px rgba(0,0,0,0.55);
  }
  .card-front {
    display: flex; align-items: center; justify-content: center; gap: 14px;
  }
  .brand-dot {
    width: 34px; height: 34px; border-radius: 50%;
    background: var(--blue);
  }
  .brand-name {
    font-family: 'Oswald', sans-serif;
    font-weight: 600;
    font-size: 44px;
    letter-spacing: 0.5px;
    text-transform: uppercase;
    color: var(--orange);
  }
  .card-back {
    display: flex; align-items: center; justify-content: center; gap: 22px;
  }
  .holder-name {
    font-family: 'Oswald', sans-serif;
    font-weight: 500;
    font-size: 30px;
    text-transform: uppercase;
    letter-spacing: 0.3px;
  }
  .holder-first { color: var(--orange); }
  .holder-last { color: var(--blue-text); }
  .divider {
    width: 2px; height: 62px; background: var(--blue);
  }
  .contact-list { list-style: none; display: flex; flex-direction: column; gap: 5px; }
  .contact-item {
    display: flex; align-items: center; gap: 8px;
    font-family: 'Roboto', sans-serif;
    font-size: 13px;
    color: var(--blue-text);
  }
  .contact-icon { width: 12px; height: 12px; flex: none; }
</style>
</head>
<body>
  <main class="stage">
    <section class="card card-front" aria-label="Card front">
      <span class="brand-dot"></span>
      <span class="brand-name">Halden's Plumbing</span>
    </section>

    <section class="card card-back" aria-label="Card back">
      <h1 class="holder-name"><span class="holder-first">Darrell</span> <span class="holder-last">Whitcombe</span></h1>
      <span class="divider"></span>
      <ul class="contact-list">
        <li class="contact-item">
          <svg class="contact-icon" viewBox="0 0 12 12"><rect x="2.5" y="0.8" width="7" height="10.4" rx="1.2" fill="none" stroke="var(--orange)" stroke-width="1.4"/><circle cx="6" cy="9.2" r="0.7" fill="var(--orange)"/></svg>
          0417305829
        </li>
        <li class="contact-item">
          <svg class="contact-icon" viewBox="0 0 12 12"><rect x="0.5" y="2" width="11" height="8" fill="var(--orange)"/><path d="M0.8 2.4 L6 6.6 L11.2 2.4" fill="none" stroke="var(--card)" stroke-width="1"/></svg>
          info@haldensplumbing.com
        </li>
        <li class="contact-item">
          <svg class="contact-icon" viewBox="0 0 12 12"><circle cx="6" cy="6" r="5.2" fill="var(--orange)"/><path d="M1 6 H11 M6 0.8 C3.5 3.5 3.5 8.5 6 11.2 M6 0.8 C8.5 3.5 8.5 8.5 6 11.2" fill="none" stroke="var(--card)" stroke-width="0.8"/></svg>
          www.haldensplumbing.com
        </li>
      </ul>
    </section>
  </main>
</body>
</html>
```